Corporate consulting business needs a business card

I want a professional business card.... surprise me

Updates

Reason: i dont think 2 days is enough

Target Market(s)

Corprorate and Not for Profit firms and organisations

Industry/Entity Type

Consulting

Contact Information for Business Card

Logo
Corporate Consulting Services
On Time, On Budget, Beyond Expectation
Tovan Presfield
Director
0427 31 94 62 (Larger)
tovan@tp-advisory.com.au
www.tp-advisory.com.au
include little icons beside the contact info:

- Envelope = email
- Phone = phone
- Globe = website

Font styles to use
Serif
Sans Serif

Requirements
Must have
• Professional and clean
Nice to have
• you tell me

```html
<!DOCTYPE html>
<html lang="en">
<head>
<meta charset="utf-8">
<title>TP Advisory – Business Card</title>
<link href="https://fonts.googleapis.com/css2?family=Cinzel:wght@500;700&family=EB+Garamond:ital,wght@0,400;0,600;1,400&display=swap" rel="stylesheet">
<style>
  :root {
    --brown: #3a2415;
    --brown-soft: #5a3b26;
    --card: #ffffff;
    --backdrop: #e9e3dc;
  }
  * { margin: 0; padding: 0; box-sizing: border-box; }
  html, body { width: 1200px; height: 913px; overflow: hidden; }
  body {
    background: var(--backdrop);
    font-family: "EB Garamond", Georgia, serif;
    color: var(--brown);
    position: relative;
  }
  .card {
    position: absolute;
    width: 560px;
    height: 320px;
    background: var(--card);
    box-shadow: 0 10px 28px rgba(58, 36, 21, 0.18);
    overflow: hidden;
  }
  .card--front { left: 50px; top: 120px; }
  .card--back { left: 590px; top: 470px; }

  /* Front */
  .front-brand {
    position: absolute; left: 0; right: 0; top: 52px;
    display: flex; align-items: center; justify-content: center; gap: 14px;
  }
  .brand-dot {
    width: 46px; height: 46px; border-radius: 50%;
    border: 4px solid var(--brown);
  }
  .brand-name {
    font-family: "Cinzel", Georgia, serif;
    font-weight: 500; font-size: 30px; letter-spacing: 2px;
    color: var(--brown);
  }
  .front-title {
    position: absolute; left: 0; right: 0; top: 140px;
    text-align: center;
    font-family: "Cinzel", Georgia, serif;
    font-weight: 700; font-size: 25px; letter-spacing: 1px;
    color: #241811;
  }
  .front-tagline {
    position: absolute; left: 0; right: 0; top: 196px;
    text-align: center;
    font-style: italic; font-size: 22px;
    color: var(--brown);
  }
  .front-rule {
    position: absolute; left: 50%; top: 240px;
    width: 260px; margin-left: -130px;
    border-top: 1.5px solid var(--brown);
  }

  /* Back */
  .back-emblem { position: absolute; left: -70px; top: -10px; }
  .back-emblem-name {
    position: absolute; left: 20px; top: 130px; width: 210px;
    text-align: center;
    font-family: "Cinzel", Georgia, serif;
    font-weight: 500; font-size: 40px; line-height: 1.05;
    color: var(--brown);
  }
  .back-details { position: absolute; left: 300px; top: 48px; width: 240px; }
  .person-name {
    font-family: "Cinzel", Georgia, serif;
    font-size: 22px; letter-spacing: 0.5px; color: var(--brown-soft);
    white-space: nowrap;
  }
  .person-name strong { font-weight: 700; color: var(--brown); }
  .person-rule { border-top: 1.5px solid var(--brown); margin: 4px 0 2px; width: 260px; }
  .person-role {
    font-family: "Cinzel", Georgia, serif;
    font-size: 12px; letter-spacing: 1px; color: var(--brown-soft);
  }
  .contact-list { list-style: none; margin-top: 24px; }
  .contact-item {
    display: flex; align-items: center; gap: 10px;
    font-size: 15px; color: #2b1d14; margin-bottom: 8px;
  }
  .contact-item--phone { font-size: 21px; }
  .contact-icon { width: 18px; height: 18px; flex: none; }
</style>
</head>
<body>

  <section class="card card--front" aria-label="Business card front">
    <div class="front-brand">
      <span class="brand-dot"></span>
      <span class="brand-name">TP Advisory</span>
    </div>
    <h1 class="front-title">CONSULTING SERVICES</h1>
    <p class="front-tagline">On Time, On Budget, Beyond Expectation</p>
    <div class="front-rule"></div>
  </section>

  <section class="card card--back" aria-label="Business card back">
    <svg class="back-emblem" width="360" height="360" viewBox="0 0 360 360" aria-hidden="true">
      <circle cx="180" cy="180" r="165" fill="none" stroke="var(--brown)" stroke-width="10"/>
    </svg>
    <div class="back-emblem-name">TP Advisory</div>

    <div class="back-details">
      <p class="person-name"><strong>TOVAN</strong> PRESFIELD</p>
      <div class="person-rule"></div>
      <p class="person-role">DIRECTOR</p>

      <ul class="contact-list">
        <li class="contact-item contact-item--phone">
          <svg class="contact-icon" viewBox="0 0 20 20" aria-hidden="true">
            <circle cx="10" cy="10" r="10" fill="var(--brown)"/>
            <path d="M6.5 5.5c.6-.6 1.3-.5 1.7.1l.9 1.4c.3.5.2 1-.2 1.4l-.5.4c.5 1.2 1.5 2.2 2.7 2.7l.4-.5c.4-.4.9-.5 1.4-.2l1.4.9c.6.4.7 1.1.1 1.7-1 1-2.5 1.1-4.4-.2-1.4-1-2.5-2.1-3.5-3.5-1.3-1.9-1.2-3.4-.2-4.4z" fill="#fff"/>
          </svg>
          0427 31 94 62
        </li>
        <li class="contact-item">
          <svg class="contact-icon" viewBox="0 0 20 20" aria-hidden="true">
            <circle cx="10" cy="10" r="10" fill="var(--brown)"/>
            <rect x="5" y="6.5" width="10" height="7" fill="#fff"/>
            <path d="M5 6.5l5 4 5-4" fill="none" stroke="var(--brown)" stroke-width="1"/>
          </svg>
          tovan@tp-advisory.com.au
        </li>
        <li class="contact-item">
          <svg class="contact-icon" viewBox="0 0 20 20" aria-hidden="true">
            <circle cx="10" cy="10" r="10" fill="var(--brown)"/>
            <g fill="none" stroke="#fff" stroke-width="1">
              <circle cx="10" cy="10" r="5.5"/>
              <ellipse cx="10" cy="10" rx="2.4" ry="5.5"/>
              <path d="M4.5 10h11M5.5 7.2h9M5.5 12.8h9"/>
            </g>
          </svg>
          www.tp-advisory.com.au
        </li>
      </ul>
    </div>
  </section>

</body>
</html>
```